Advert for Services that we offer

Brenwick Torque Ltd need an design to represent what we do in a modern way by showing an image with a brief description and the use of corporate logo the information we will proved vie a doc file and this is to be presented in a modern way. This design will be for print & web. we have done our own design and its not great i have put this in the file repository

Target Market(s)

Motor trade

Font styles to use
Sans Serif

Colors

Designer to choose colors to be used in the design.

Requirements
Must have
• Company colour scheme as per logo within the files uploaded.
• and a small boarder to isolate it from the rest of the articles.
Nice to have
• Modern font
Should not have
• Old style font

```html
<!DOCTYPE html>
<html lang="en">
<head>
<meta charset="utf-8">
<title>Brenwick Torque Ltd – Product testing &amp; analysis</title>
<link href="https://fonts.googleapis.com/css2?family=Noto+Sans:wght@400;700&display=swap" rel="stylesheet">
<style>
  :root {
    --brand-blue: #2474ba;
    --brand-grey: #a7a8ab;
    --text-grey: #45474b;
    --paper: #ffffff;
    --photo-light: #c9c9c7;
    --photo-mid: #7d7e80;
    --photo-dark: #3c3d40;
  }
  html, body {
    margin: 0;
    padding: 0;
    width: 1200px;
    height: 1200px;
    overflow: hidden;
    background: var(--paper);
    font-family: "Noto Sans", "Droid Sans", sans-serif;
  }
  .canvas {
    position: relative;
    width: 1200px;
    height: 1200px;
  }
  .banner {
    position: absolute;
    left: 33px;
    top: 125px;
    width: 1140px;
    height: 651px;
    box-sizing: border-box;
    border: 11px solid var(--brand-blue);
    border-radius: 20px;
    background: var(--paper);
    overflow: hidden;
  }
  .service-photo {
    position: absolute;
    inset: 0;
    background: linear-gradient(110deg, var(--photo-light) 0%, var(--photo-mid) 45%, var(--photo-dark) 75%);
    clip-path: polygon(300px 0, 100% 0, 100% 100%, 568px 100%);
  }
  .brand-name {
    position: absolute;
    left: 56px;
    top: 100px;
    width: 240px;
    margin: 0;
    text-align: center;
    font-size: 26px;
    line-height: 1.15;
    font-weight: 700;
    color: var(--brand-blue);
  }
  .service-heading {
    position: absolute;
    left: 32px;
    top: 219px;
    margin: 0;
    font-size: 25px;
    line-height: 34px;
    font-weight: 700;
    color: var(--text-grey);
  }
  .service-list {
    position: absolute;
    left: 32px;
    top: 327px;
    margin: 0;
    padding: 0;
    list-style: none;
    font-size: 25px;
    line-height: 34.4px;
    font-weight: 400;
    color: var(--text-grey);
  }
  .service-list li::before {
    content: "·";
  }
  .contact-band {
    position: absolute;
    left: 12px;
    top: 542px;
    width: 425px;
    height: 76px;
  }
  .contact-phone {
    position: absolute;
    left: 32px;
    top: 558px;
    margin: 0;
    font-size: 25px;
    line-height: 30px;
    color: var(--paper);
  }
  .contact-web {
    position: absolute;
    left: 142px;
    top: 590px;
    margin: 0;
    font-size: 15px;
    line-height: 18px;
    color: var(--paper);
  }
</style>
</head>
<body>
  <div class="canvas">
    <section class="banner">
      <div class="service-photo" role="img" aria-label="Photo of a technician in a workshop measuring the bore of a red-painted flanged hub with a digital gauge"></div>

      <p class="brand-name">Brenwick Torque Ltd</p>

      <h1 class="service-heading">Heading:<br>Product testing &amp; analysis</h1>

      <ul class="service-list">
        <li>Metallurgical testing</li>
        <li>Bearing pre-load testing</li>
        <li>Bore measurement</li>
        <li>New product evaluation</li>
        <li>Product analysis &amp; report</li>
      </ul>

      <svg class="contact-band" viewBox="0 0 425 76" aria-hidden="true">
        <polygon points="0,0 358,0 411,64 0,64" fill="var(--brand-grey)"/>
        <path d="M0,11 H353 L408,75 H8 Q0,75 0,67 Z" fill="var(--brand-blue)"/>
      </svg>
      <p class="contact-phone">TEL : +44 (0) 161 555 0192</p>
      <p class="contact-web">www.brenwick-torque.co.uk</p>
    </section>
  </div>
</body>
</html>
```